Need somewhat upscale, eye catching honey jar label to make our product stand out on store shelves.

We need front and back labels for a honey jar. Files "Honey Jar Front Label 2" & "Honey Jar Back Label 2" show what I have come up with.

Files "Honey Jar Front Label 2". I did this as an example. It shows the information that needs to be included on the front label. The picture was taken by my daughter. The information and picture can be rearranged, enlarged, reduced, cropped, etc. as you see fit.

Files "Honey Jar Back Label 2". I did this one to play with the wording to get the information to fit. It explains how I keep bees. It can be worded differently as long as all the information is included.

I know nothing about good use of color, borders, backgrounds, font style and size, etc. so please excuse my plain presentations. I admire and respect your creative abilities very much.

Since my method of keeping bees involves a lot of travel time and expense, as mentioned in files "Honey Jar Back Label 2" I will try to price my honey a little higher than the competition so please design accordingly with that in mind.

We think we want to use a traditional jar with stick on labels like Marlow's jar seen in file Marlow's Jar. However, feel free to use a different jar as long as the honey can be easily scooped out with a spoon and does not have to be poured out. I know that eliminates a lot of fancy jars but that's what my customers want. Jar size should be 12 ounces which will hold a little more than 1 pound of honey.

Hanging labels are also acceptable therefore jar shapes that will not accept a stick on label can also be used. An example is a Honeypot Jar.

And of course we like Hexagon Jars which are 6 sided like the cells in honeycomb.

Please stick to glass jars that are readily available. No custom shaped jars for now.

Marlow's jar is clear glass and the metal lid is a light golden color.

It's probably a good idea for the shape of the labels to match the shape of the bottle like I marked in black on Marlow's Jar. Being wider in the middle should allow the back label to be shorter than my example seen in files "Honey Jar Back Label 2". I think front and back labels should be the same size.

The shape of the area marked in black around Marlow's label measures 1-1/4 (1.25) inches across the top, 2-1/4 (2.25) inches across the middle, 2 inches across the bottom and 3-1/2 (3.5) inches tall from top to bottom.

Target Market(s)

People wanting local honey that is not processed in any way.
People that are willing to pay a little more for honey from bees that are kept in a sustainable way (see the story in files 2 & 17) without the use of harsh chemicals.

Industry/Entity Type

Travel

Font styles to use
Serif
Decorative
Script

Requirements
Must have
• See my lengthy project description, file "Honey Jar Front Label 2" and file "Honey Jar Back Label 2". All of the info. therein is very important.
• Somewhat upscale, eye catching appearance that makes the product stand out on store shelves and suggests that the honey inside is quality, unprocessed truly local honey.
Nice to have
• If bullets are used they can look like a skep (type of beehive). I have included an example in a file.
• Swirly dashed line coming off the s in lin-Wren's with a honeybee at the end of it. See files for examples.
• Swirly dashed line coming off the i in wildflower making the shape of a heart with a honeybee at the end of it hovering over the o in wildflower and the o looks like a flower. See files for examples.

```html
<!DOCTYPE html>
<html lang="en">
<head>
<meta charset="utf-8">
<title>lin-Wren's Local Honey – Back Label</title>
<link rel="stylesheet" href="https://fonts.googleapis.com/css2?family=Cherry+Swash:wght@700&display=swap">
<style>
  :root {
    --red-deep: #7e0609;
    --red-mid: #a0101a;
    --amber-low: #b8301a;
    --amber-warm: #c85420;
    --white: #ffffff;
    --gold: #f3b800;
    --link: #ffff33;
    --panel: rgba(255, 225, 225, 0.32);
    --text-shadow: 1px 1px 1px #3a0000, 0 0 3px rgba(60, 0, 0, 0.7);
  }
  * { margin: 0; padding: 0; box-sizing: border-box; }
  html, body { width: 771px; height: 1200px; overflow: hidden; background: var(--red-deep); }
  .label {
    position: relative;
    width: 771px;
    height: 1200px;
    overflow: hidden;
    font-family: "Cherry Swash", Georgia, serif;
    font-weight: 700;
    color: var(--white);
    text-shadow: var(--text-shadow);
    text-align: center;
  }
  .band-top {
    position: absolute; left: 0; top: 0; width: 771px; height: 451px;
    background: radial-gradient(ellipse at 50% 25%, #a00d12 0%, var(--red-deep) 75%);
  }
  .band-middle {
    position: absolute; left: 0; top: 451px; width: 771px; height: 431px;
    background: var(--red-mid);
  }
  .band-bee-photo {
    position: absolute; left: 0; top: 882px; width: 771px; height: 318px;
    background: radial-gradient(ellipse at 30% 55%, #d06a3a 0%, var(--amber-warm) 30%, var(--amber-low) 75%, #a82414 100%);
  }
  .brand {
    position: absolute; left: 0; top: 48px; width: 771px;
    font-size: 30px; line-height: 40px;
    font-weight: 700;
    color: var(--white);
    text-shadow: none;
  }
  .story {
    position: absolute; left: 0; top: 140px; width: 771px;
    font-size: 21.5px; line-height: 28.6px;
  }
  .story .section-title { color: var(--gold); }
  .story .star { color: var(--gold); }
  .story .site { color: var(--link); }
  .panel {
    position: absolute;
    background: var(--panel);
    border-radius: 28px;
    font-size: 20.5px; line-height: 28.6px;
  }
  .panel-serving { left: 207px; top: 693px; width: 357px; height: 189px; padding-top: 9px; }
  .panel-amounts { left: 244px; top: 894px; width: 289px; height: 216px; padding-top: 3px; }
  .panel-title { color: var(--gold); }
  .facts { text-align: left; margin-left: 22px; }
  .facts .row { display: flex; }
  .facts .name { width: 179px; white-space: nowrap; }
  .facts .indent { padding-left: 85px; }
</style>
</head>
<body>
<main class="label">
  <div class="band-top"></div>
  <div class="band-middle"></div>
  <div class="band-bee-photo" role="img" aria-label="Close-up photo of a honeybee over honeycomb in warm orange-red tones"></div>

  <h1 class="brand">lin-Wren's<br>Local Honey</h1>

  <section class="story">
    <p>Bees kept in Cobb, Cherokee, DeKalb, Douglas,<br>Forsyth, Gwinnett, Hall &amp; Jackson Counties.</p>
    <p>&nbsp;</p>
    <p class="section-title">Sustainable Beekeeping</p>
    <p>* Partnering with local farmers and landowners<br>
    we spread our bees out over many square miles,<br>
    keeping fewer bees at more locations. Although<br>
    much more time consuming and expensive, it<br>
    allows the pollinators to benefit more of the envi-<br>
    ronment and ensures them more abundant natu-<br>
    ral food. This eliminates the need to feed cane<br>
    sugar or high fructose corn syrups which results<br>
    in healthier bees and purer honey, not<br>
    contaminated with syrup.</p>
    <p><span class="star">*</span> We will never sacrifice the health of the bees or<br>
    the quality of their honey for profit. Never!</p>
    <p><span class="star">*</span> We sell honey from our bees only.</p>
    <p><span class="star">*</span> Do not feed to infants under 1 year old.</p>
    <p class="site">http://lin-Wrens.com</p>
  </section>

  <section class="panel panel-serving">
    <p class="panel-title">Nutrition Facts</p>
    <p>Serv. Size 1 Tbsp (21g)</p>
    <p>Serv. Per Container 21</p>
    <p>&nbsp;</p>
    <p>Percent Daily Values (DV) are<br>based on a 2,000 calorie diet.</p>
  </section>

  <section class="panel panel-amounts">
    <p class="panel-title">Amount Per Serving</p>
    <p>Calories 64</p>
    <div class="facts">
      <div class="row"><span class="name">Total Fat &nbsp; 0g</span><span class="dv">0% DV</span></div>
      <div class="row"><span class="name">Sodium &nbsp; 0mg</span><span class="dv">0% DV</span></div>
      <div class="row"><span class="name">Total Carbs17g</span><span class="dv">6% DV</span></div>
      <div class="row"><span class="indent">Sugars 16g</span></div>
      <div class="row"><span class="name">Protein 0g</span><span class="dv">0% DV</span></div>
    </div>
  </section>
</main>
</body>
</html>
```